Business Card for Lawyer

I'm looking for a business card for my new law firm, based in Ontario, Canada. I would prefer single sided. I am partial (but not limited) to white and blue color wise and like things understated. Also, if you can work in the red KT rating symbol from Penrowe-Calloway, that would be a plus.

Target Market(s)

Old people - so it should be easy to read.

Industry/Entity Type

Business

Contact Information for Business Card

See the specs in the word document below. Also, see the design for my website. The card should have a similar look to the site.

Requirements
Must have
• Everything listed in the business card specs. I don't mind having the address set off at the bottom of the card on its own line.
Should not have
• 1) Any sort of design that could also be used by a tattoo parlour or a tarot card reader, mystic etc.
• 2) There should not be any photographs of me (or anyone else).

```html
<!DOCTYPE html>
<html lang="en">
<head>
<meta charset="utf-8">
<title>Darrow's Law Firm – Business Card</title>
<link rel="stylesheet" href="https://fonts.googleapis.com/css2?family=Libre+Baskerville:ital@0;1&family=Open+Sans:wght@400;600;700&display=swap">
<style>
  :root {
    --bg: #d9dbde;
    --card: #ffffff;
    --navy: #24506e;
    --navy-dark: #1b3d55;
    --blue-text: #1f5a80;
    --ink: #2b4a63;
    --body: #2d3338;
    --grey-light: #e9eaeb;
    --grey-mid: #a9acaf;
    --grey-dark: #8c9094;
    --rule: #3a3f44;
    --badge: #f3d3d4;
    --white: #ffffff;
  }
  * { box-sizing: border-box; margin: 0; padding: 0; }
  html, body { width: 1200px; height: 800px; overflow: hidden; }
  body { background: var(--bg); position: relative; font-family: "Open Sans", sans-serif; }

  .card {
    position: absolute; left: 110px; top: 120px;
    width: 980px; height: 560px;
    background: var(--card);
    border-radius: 24px;
    overflow: hidden;
    box-shadow: 0 10px 30px rgba(0,0,0,.18);
  }
  .card__top-band { position: absolute; left: 0; top: 0; width: 100%; height: 22px; background: var(--navy); }

  .header {
    position: absolute; left: 0; top: 22px; width: 100%; height: 178px;
    background: linear-gradient(160deg, var(--grey-light) 0%, var(--grey-mid) 55%, var(--grey-dark) 100%);
    border-bottom: 2px solid var(--rule);
  }
  .brand { position: absolute; left: 40px; top: 22px; display: flex; align-items: center; gap: 16px; }
  .brand__mark { width: 64px; height: 64px; background: var(--white); border: 3px solid var(--ink); }
  .brand__name {
    font-family: "Libre Baskerville", serif; color: var(--white);
    font-size: 30px; line-height: 1.05; letter-spacing: 2px; text-transform: uppercase;
  }
  .slogan {
    position: absolute; right: 40px; top: 96px;
    font-family: "Libre Baskerville", serif; font-style: italic;
    color: var(--white); font-size: 22px;
  }
  .services {
    position: absolute; right: 40px; top: 138px;
    color: var(--blue-text); font-weight: 700; font-size: 21px; letter-spacing: .2px;
  }
  .services span { color: var(--body); font-weight: 400; margin: 0 6px; }

  .person { position: absolute; left: 40px; top: 224px; }
  .person__name {
    font-family: "Libre Baskerville", serif; color: var(--ink);
    font-size: 32px; font-variant: small-caps; letter-spacing: 1px;
  }
  .person__name small { font-size: 20px; font-variant: normal; letter-spacing: 0; }
  .person__title {
    font-family: "Libre Baskerville", serif; color: var(--body);
    font-size: 15px; letter-spacing: 1px; margin-top: 4px;
  }

  .contacts { position: absolute; left: 40px; top: 310px; list-style: none; }
  .contacts li { display: flex; align-items: center; gap: 14px; font-size: 21px; color: var(--body); height: 32px; }
  .contacts svg { width: 22px; height: 22px; flex: none; }

  .rating-badge {
    position: absolute; right: 40px; top: 376px;
    width: 300px; height: 96px;
    background: var(--badge);
    border-radius: 6px;
  }

  .footer {
    position: absolute; left: 0; bottom: 0; width: 100%; height: 70px;
    background: var(--navy); border-top: 2px solid var(--navy-dark);
    display: flex; align-items: center; padding-left: 40px;
    color: var(--white); font-weight: 600; font-size: 22px; letter-spacing: .5px; text-transform: uppercase;
  }
</style>
</head>
<body>
  <article class="card">
    <div class="card__top-band"></div>

    <header class="header">
      <div class="brand">
        <div class="brand__mark"></div>
        <div class="brand__name">Darrow's<br>Law Firm</div>
      </div>
      <p class="slogan">“Getting the results that matter!”</p>
      <p class="services">Personal Injury<span>|</span>Malpractice<span>|</span>Insurance<span>|</span>Business Litigation</p>
    </header>

    <section class="person">
      <h1 class="person__name">Daniel R. Whitcombe, <small>B.A. &amp; J.D.</small></h1>
      <p class="person__title">LAWYER</p>
    </section>

    <ul class="contacts">
      <li>
        <svg viewBox="0 0 22 22" aria-hidden="true"><rect width="22" height="22" rx="4" fill="var(--navy)"/><path d="M7 5l2.5 0 1 3-1.5 1.2a8 8 0 0 0 3.8 3.8L14 11.5l3 1v2.5A1.5 1.5 0 0 1 15.5 16.5 10.5 10.5 0 0 1 5.5 6.5 1.5 1.5 0 0 1 7 5z" fill="#fff"/></svg>
        647-555-0142
      </li>
      <li>
        <svg viewBox="0 0 22 22" aria-hidden="true"><rect width="22" height="22" rx="4" fill="var(--navy)"/><rect x="5" y="9" width="12" height="8" rx="1" fill="#fff"/><rect x="7" y="5" width="8" height="5" fill="#fff" stroke="var(--navy)" stroke-width="1"/></svg>
        647-555-0187
      </li>
      <li>
        <svg viewBox="0 0 22 22" aria-hidden="true"><rect width="22" height="22" rx="4" fill="var(--navy)"/><rect x="5" y="7" width="12" height="9" fill="#fff"/><path d="M5 7l6 5 6-5" fill="none" stroke="var(--navy)" stroke-width="1.3"/></svg>
        daniel@darrowsfirm.ca
      </li>
      <li>
        <svg viewBox="0 0 22 22" aria-hidden="true"><rect width="22" height="22" rx="4" fill="var(--navy)"/><rect x="5" y="6" width="12" height="10" fill="#fff"/><rect x="5" y="6" width="12" height="2.5" fill="#9fb6c7"/></svg>
        www.darrowsfirm.ca
      </li>
    </ul>

    <div class="rating-badge" role="img" aria-label="Peer review rating badge from Penrowe-Calloway"></div>

    <footer class="footer">12 Harbour Street East, Ground Floor, Hamilton, ON L8N 4K2</footer>
  </article>
</body>
</html>
```